Arzt im ästhetischen Bereich sucht seriöses Flyer-Design
Zielgruppe
Ich bin Arzt und nebenberuflich mache ich Eingriffe im ästhetischen Bereich (Lumex- und Hyaluronunterspritzung, Lipolyse, Eigenblutbehandlung (PRP) bzw. Perlglanzkur).
Ich möchte gerne einen sechsseitigen Flyer mit Falz. Auf der Deckseite sollte ein schönes Logo mit ästhetischen Bezug stehen, auf den anderen Seiten werden je die Behandlungsmethoden erklärt (Text kann ich zusteuern bzw. füge ich nach Erhalt des Designs ein). Es sollten auf jeder Seite schöne Abbildungen (entweder Fotomaterial oder auch Zeichnungen) der Methoden enthalten sein. Auf der letzten Seite sollen meine Kontaktdaten stehen
Aufgabenstellung
s.o. 6 seitiger Flyer mit Falzen. Farbe frei. Design medizinisch-ästhetisch mit seriösen Eindruck. Logo von mir soll auf der Rückseite mit meinen Kontaktdaten eingefügt werden.

```html
<!DOCTYPE html>
<html lang="de">
<head>
<meta charset="utf-8">
<title>Flyer Innenseite – Lipolyse &amp; Hyaluron</title>
<link href="https://fonts.googleapis.com/css2?family=Raleway:wght@400;500;700&display=swap" rel="stylesheet">
<style>
  :root {
    --stage: #d9d9d9;
    --paper: #ffffff;
    --sky: #47b1e0;
    --ink: #2f4656;
    --heading: #3a5466;
    --wave-light: #7fc6e8;
    --wave-dark: #2a4658;
    --skin-light: #f6ece6;
    --skin-mid: #e9d2c4;
  }
  * { margin: 0; padding: 0; box-sizing: border-box; }
  html, body { width: 1200px; height: 676px; overflow: hidden; }
  body { background: var(--stage); font-family: "Raleway", sans-serif; color: var(--ink); }
  .flyer {
    position: absolute; left: 151px; top: 9px;
    width: 899px; height: 636px;
    background: var(--paper); overflow: hidden;
  }
  .top-band { position: absolute; left: 0; top: 0; width: 100%; height: 20px; background: var(--sky); }
  .photo-waist {
    position: absolute; left: 0; top: 20px; width: 276px; height: 325px;
    background: linear-gradient(180deg, #f1ddd3 0%, #f4e6df 55%, rgba(255,255,255,0) 100%);
  }
  .photo-face {
    position: absolute; left: 276px; top: 20px; width: 623px; height: 265px;
    background: linear-gradient(90deg, #ffffff 0%, #f8f2ee 35%, var(--skin-light) 60%, var(--skin-mid) 85%, #e3c7b6 100%);
  }
  .wave { position: absolute; left: 0; top: 0; width: 899px; height: 636px; }
  .section-title {
    position: absolute; font-weight: 700; font-size: 16px; line-height: 20px;
    color: var(--heading); text-decoration: underline; text-underline-offset: 2px;
    white-space: nowrap;
  }
  .section-title .note { font-weight: 400; text-decoration: none; }
  .copy {
    position: absolute; font-size: 10.9px; line-height: 12.8px; font-weight: 400;
    white-space: nowrap;
  }
  .copy p + p { margin-top: 12.8px; }
  .lipo-title { left: 20px; top: 252px; letter-spacing: -0.8px; }
  .lipo-copy { left: 20px; top: 284px; }
  .hya-title { left: 314px; top: 302px; letter-spacing: -0.3px; }
  .hya-copy { left: 315px; top: 336px; }
  .hya-copy-2 { left: 618px; top: 336px; }
</style>
</head>
<body>
<main class="flyer">
  <div class="top-band"></div>
  <div class="photo-waist" role="img" aria-label="Foto: Hand misst Taille mit Maßband"></div>
  <div class="photo-face" role="img" aria-label="Foto: Frau berührt ihr Gesicht"></div>

  <svg class="wave" viewBox="0 0 899 636" aria-hidden="true">
    <defs>
      <linearGradient id="waveFill" x1="0" y1="0" x2="1" y2="0">
        <stop offset="0" stop-color="#7fc6e8"/>
        <stop offset="0.5" stop-color="#5b97b2"/>
        <stop offset="1" stop-color="#2a4658"/>
      </linearGradient>
    </defs>
    <path d="M0 583 C 420 562, 820 520, 899 437 L 899 636 L 0 636 Z" fill="url(#waveFill)"/>
  </svg>

  <h2 class="section-title lipo-title">Lipolyse-Therapie („Fettwegspritze“<span class="note">)</span></h2>
  <div class="copy lipo-copy">
    <p>Die Injektions-Lipolyse dient dem Abschmelzen<br>kleinerer hartnäckiger Fettpolster (v.a. Hüpft-,<br>Bauch-, „Reiterhosen-“, Oberarm- und Halsbe-<br>reich), die durch Umstellung der Ernährung und<br>sportliche Betätigung nicht zu beseitigen sind.</p>
    <p>Der Wirkstoff Phosphatidylcholin wird mittels<br>feinster Nadeln direkt in das Fettgewebe injiziert.<br>Durch die Injektionen setzt der behandelnde Arzt<br>eine künstliche Entzündung, die eine zusätzliche<br>Straffung der Haut bewirkt.</p>
    <p>Um ein optimales Ergebnis zu erzielen, sind 1 bis<br>max. 4 Behandlungssitzungen notwendig, nach 6<br>Monaten wird der Behandlungserfolgt überprüft<br>und ist von der Konsistenz der behandelten Fett-<br>polster abhängig.</p>
    <p>Ca. 80% der behandelten Patienten sind mit der<br>Behandlung sehr zufrieden. In den ersten Tagen<br>können Schwellungen und Blutergüsse auftreten,<br>die im Verlauf vollständig verschwinden.</p>
  </div>

  <h2 class="section-title hya-title">Hyaluron-Behandlung</h2>
  <div class="copy hya-copy">
    <p>Hyaluron ist ein wichtiger Bestandteil des Binde-<br>gewebes und auch für die Zellfunktion notwendig.<br>Weiterhin ist Hyaluron für die Wasserspeicherung<br>und somit Elastizität der Haut entscheidend. Größere<br>und tiefere Falten, bei denen eine Lumex-Behand-<br>lung nicht sinnvoll bzw. nicht möglich erscheint,<br>eignen sich hervorragend für die Hyaluron-Therapie.</p>
    <p>Mittels kleinster Injektionen wird die Faltenregion<br>mit Hyaluron unterfüllt und somit geglättet. Das<br>Ergebnis ist sofort sichtbar, weitere Korrekturen<br>können umgehend oder im Verlauf durchgeführt<br>werden.</p>
  </div>
  <div class="copy hya-copy-2">
    <p>Typische Anwendungsgebiete sind die<br>Nasolabialfalte, Glabella, Falten im Bereich von<br>Unterlid, Tränenkanal und Mund-(winkel) sowie<br>das Auffüllen der Lippen bzw. des Lippenbogens<br>(„Lippen-Augmentation“). Da es sich um einen<br>körpereigenen Stoff handelt sind keine nennenswer-<br>ten Risiken zu erwarten. Im Verlauf wird das einge-<br>brachte Hyaluron vom Körper abgebaut, eine<br>Wirkdauer von 6-12 Monatenist zu erwarten.</p>
  </div>
</main>
</body>
</html>
```